The Deskwell (A new and exciting small Business support solution) Business Cards

The Deskwell Business Card Design

About us:
The Deskwell is a small business support solution, assisting businesses with any marketing, office management and human resource skills.

Objective
To be a small business lifesaver, to relieve busy professionals from mundane operations so they can focus on their businesses future through complete, reliable, efficient and effective client support. To have people say WOW what did we do before The Deskwell.

Industry/Entity Type

Small Business

Colors
0355a3
33a6d7

Requirements
Must have
• Must be similar to the look and feel of my website http://www.thedeskwell-example.com.au/

Must have:

Blue colour is 0094FF

The Logo

A Small Business Support Solution
- Human Resources
- Office Administration
- Marketing

Maribel Torvik
0462 837 105
maribeltorvik@thedeskwell-example.com.au
www.thedeskwell-example.com

```html
<!DOCTYPE html>
<html lang="en">
<head>
<meta charset="utf-8">
<title>The Deskwell – Business Cards</title>
<link rel="stylesheet" href="https://fonts.googleapis.com/css2?family=Open+Sans:wght@400;600&display=swap">
<style>
  :root {
    --bg: #e9eaec;
    --card: #ffffff;
    --brand-blue: #0094ff;
    --panel-blue: #4a8fd8;
    --ink: #111418;
    --muted: #5b6168;
    --shadow: rgba(0, 0, 0, 0.18);
  }
  * { box-sizing: border-box; margin: 0; padding: 0; }
  html, body {
    width: 1200px;
    height: 1000px;
    overflow: hidden;
    background: var(--bg);
    font-family: "Open Sans", Arial, sans-serif;
  }
  .sheet {
    position: relative;
    width: 1200px;
    height: 1000px;
  }
  .card {
    position: absolute;
    left: 320px;
    width: 560px;
    height: 320px;
    background: var(--card);
    box-shadow: 0 8px 24px var(--shadow);
    overflow: hidden;
  }
  .card--front { top: 100px; }
  .card--back { top: 560px; }

  /* Front */
  .front-lockup {
    position: absolute;
    left: 0; right: 0;
    top: 112px;
    text-align: center;
  }
  .wordmark {
    font-size: 54px;
    font-weight: 400;
    letter-spacing: -1px;
    line-height: 1;
    color: var(--ink);
  }
  .tagline {
    margin-top: 8px;
    font-size: 17px;
    font-weight: 400;
    letter-spacing: 1.5px;
    color: var(--brand-blue);
  }

  /* Back */
  .back-wordmark {
    position: absolute;
    left: 30px;
    top: 34px;
    font-size: 34px;
    letter-spacing: -0.5px;
    color: var(--ink);
  }
  .services {
    position: absolute;
    right: 0;
    top: 112px;
    width: 196px;
    padding: 12px 16px;
    background: var(--panel-blue);
    list-style: none;
    color: #ffffff;
    font-size: 12px;
    line-height: 1.45;
  }
  .contact {
    position: absolute;
    left: 30px;
    bottom: 56px;
    font-size: 11.5px;
    line-height: 1.55;
    color: var(--muted);
  }
  .contact .name {
    font-size: 14px;
    font-weight: 600;
    color: var(--brand-blue);
    margin-bottom: 2px;
  }
  .base-band {
    position: absolute;
    left: 0; right: 0; bottom: 0;
    height: 36px;
    background: var(--panel-blue);
  }
</style>
</head>
<body>
<main class="sheet">
  <section class="card card--front" aria-label="Business card front">
    <div class="front-lockup">
      <div class="wordmark">The Deskwell</div>
      <div class="tagline">A Small Business Support Solution</div>
    </div>
  </section>

  <section class="card card--back" aria-label="Business card back">
    <div class="back-wordmark">The Deskwell</div>
    <ul class="services">
      <li>Marketing Administration</li>
      <li>Office Management</li>
      <li>Human Resources</li>
      <li>Administration</li>
    </ul>
    <address class="contact">
      <div class="name">Maribel Torvik</div>
      <div>0462 837 105</div>
      <div>maribeltorvik@thedeskwell-example.com.au</div>
      <div>www.thedeskwell-example.com</div>
    </address>
    <div class="base-band"></div>
  </section>
</main>
</body>
</html>
```